New Postcard Design Project for home loan

The project is for home loan for business owners that do no need to have any income statements. NO W2, NO TAX RETURNS, NO PAYSTUBS , CALL /TEXT/EMAIL DORIAN KELT DKELT@PELVORAFUNDING.COM 502.647.2913

GET LICENSE INFORMATION FROM WEBSITE:

Here is the information you will need to have on the mailer:

- LO Name
- LO NMLS
- Branch Name (if applicable)
- Branch NMLS (if applicable)
- Branch Address (if applicable)
- Pelvora Corporation
- Pelvora NMLS
- Pelvora Address
- Pelvora Phone Number

And since you’re going to be talking about rates, you will need the following information as well:
1. Amount of the represented loan.
2. Repayment term in years of the represented loan.
3. Prepayment terms.
4. If the advertised rate may increase, the ad must state: "Advertised rate may increase"
5. Statement: "Restrictions may apply. Programs not available in all areas."

Target Market(s)

home owners that own a business

Industry/Entity Type

Home Loan refinance

Font styles to use
Serif

Colors
59FF00
82FF00
B8FF75
E3FFCB
F4FFEA
F0912C
F2A743
F7CA91
FBE8D2
FDF5EE
EE7325
F08F49
F5BC92
FAE3D3
FDF4ED
EB3D1F
EC4F4E
F09395
F8D3D4
FCEDEE

Requirements
Must have
• Must have No W2, No Tax Returns, No Paystubs Required. Must have picture of home. Home loans for business owners without traditional tax returns. MUST HAVE LOAN DISCLOSURES.
Nice to have
• Pictures of Home loan Make the customer Call the loan officer. 502.647.2913
Should not have
• My website you can extract logo: https://www.pelvorafunding.com/doriankelt

```html
<!DOCTYPE html>
<html lang="en">
<head>
<meta charset="utf-8">
<title>Pelvora Home Loan Postcard</title>
<link rel="stylesheet" href="https://fonts.googleapis.com/css2?family=Oswald:wght@700&family=Lato:wght@400;700&family=Montserrat:wght@700&display=swap">
<style>
:root{
  --stage:#4a4a4c;
  --navy:#1d3a6e;
  --sky:#2ea8e0;
  --swoosh-blue:#4a9ad4;
  --orange:#f2a743;
  --white:#ffffff;
  --ink:#111111;
  --stamp:#e8e8e8;
}
*{margin:0;padding:0;box-sizing:border-box}
html,body{width:1200px;height:1200px;overflow:hidden;background:var(--stage)}
.stage{position:relative;width:1200px;height:1200px}
.card{position:absolute;background:var(--white);overflow:hidden}
.card-bg{position:absolute;inset:0;width:100%;height:100%}
.front{left:102px;top:81px;width:625px;height:484px}
.back{left:481px;top:635px;width:634px;height:491px}

.headline{position:absolute;font-family:"Oswald",sans-serif;font-weight:700}
.front .headline{left:17px;top:12px;color:var(--white);font-size:34px;line-height:37px;text-transform:uppercase}
.back .headline{left:17px;top:20px;color:var(--navy);font-size:19px;line-height:23px}

.logo-mark{position:absolute;left:422px;top:224px;width:108px;height:108px;display:flex;align-items:center;justify-content:center;
  font-family:"Lato",sans-serif;font-weight:700;font-size:19px;color:var(--navy)}

.officer{position:absolute;left:24px;top:367px;font-family:"Lato",sans-serif;color:var(--navy)}
.officer .contact{font-size:17px;line-height:22px}
.officer .name{font-size:27px;line-height:30px;font-weight:700}
.officer .title{font-size:18px;line-height:22px;font-weight:700;color:var(--ink)}
.officer .nmls{font-size:18px;line-height:22px;color:var(--ink)}
.divider{position:absolute;left:172px;top:366px;width:2px;height:104px;background:var(--sky)}

.company{position:absolute;left:191px;top:364px;width:200px;font-family:"Lato",sans-serif;color:var(--navy)}
.company .corp{font-size:14.5px;line-height:17px;font-weight:700}
.company .corp-nmls{font-size:14.5px;line-height:17px;font-weight:700;margin-top:3px}
.company .address{font-size:12.5px;line-height:15px;color:var(--ink);margin-top:3px}

.reach{position:absolute;left:422px;top:389px;font-family:"Lato",sans-serif;color:var(--white)}
.reach .lines{font-size:12.5px;line-height:15px}
.reach .phone{display:flex;align-items:center;gap:6px;margin-top:7px;font-size:22px;font-weight:700;letter-spacing:.3px}
.phone-icon{width:22px;height:22px;flex:none}

.stamp{position:absolute;left:541px;top:16px;width:76px;height:66px;background:var(--stamp)}
.address-line{position:absolute;left:396px;width:209px;height:2px;background:var(--ink)}

.disclosures{position:absolute;left:17px;top:226px;width:275px;font-family:"Lato",sans-serif;color:var(--white);font-size:16px;line-height:16px;list-style:none}
.disclosures li{display:flex;margin-bottom:6px}
.disclosures .num{width:15px;flex:none}
.disclosures .note{display:block;font-size:12px;line-height:15px;margin-top:2px}

.cta{position:absolute;left:18px;top:439px;display:flex;align-items:center;gap:3px;font-family:"Montserrat",sans-serif;font-weight:700;font-size:18px;color:var(--navy)}
.cta .phone-icon{width:23px;height:23px}
</style>
</head>
<body>
<main class="stage">

  <section class="card front">
    <svg class="card-bg" viewBox="0 0 625 484">
      <defs>
        <linearGradient id="house-tones" x1="0" y1="0" x2="0" y2="1">
          <stop offset="0" stop-color="#5a9bd6"/>
          <stop offset=".3" stop-color="#6ea5da"/>
          <stop offset=".5" stop-color="#3f6aa6"/>
          <stop offset=".66" stop-color="#2f4f82"/>
          <stop offset=".8" stop-color="#cfc6b8"/>
          <stop offset=".92" stop-color="#a3978a"/>
          <stop offset="1" stop-color="#5d6450"/>
        </linearGradient>
      </defs>
      <path class="navy-panel" d="M543,0 C600,60 610,180 476,278 C420,330 395,400 394,484 L625,484 L625,0 Z" fill="var(--navy)"/>
      <path class="blue-swoosh" d="M440,300 C392,350 380,410 378,484 L394,484 C395,400 420,330 476,278 Z" fill="var(--swoosh-blue)"/>
      <path class="house-photo" role="img" aria-label="Photo of a modern two-storey luxury home at dusk" d="M0,0 L548,0 C610,70 590,200 470,262 C400,305 300,335 208,334 C120,333 50,300 0,262 Z" fill="url(#house-tones)"/>
      <path class="sky-band" d="M0,262 C50,300 120,333 208,334 C300,335 400,305 470,262 L470,282 C400,325 300,350 208,350 C110,350 40,318 0,286 Z" fill="var(--sky)"/>
      <path class="orange-rule" d="M190,336 C300,336 390,310 450,276" fill="none" stroke="var(--orange)" stroke-width="3"/>
      <path class="orange-swoosh" d="M520,0 L566,0 C650,90 610,210 500,262 L486,250 C585,190 590,70 520,0 Z" fill="var(--orange)"/>
      <path class="orange-line" d="M578,0 C600,90 580,180 518,242" fill="none" stroke="var(--orange)" stroke-width="2"/>
      <path class="orange-line" d="M442,318 C415,360 412,420 422,484" fill="none" stroke="var(--orange)" stroke-width="2"/>
      <circle cx="476" cy="278" r="53" fill="var(--white)" stroke="var(--orange)" stroke-width="6"/>
    </svg>

    <h1 class="headline">No W2 I No Tax Returns<br>No Paystubs Required</h1>
    <div class="logo-mark">Pelvora</div>

    <div class="officer">
      <p class="contact">Contact Dorian</p>
      <p class="name">Dorian Kelt</p>
      <p class="title">Branch Manager</p>
      <p class="nmls">NMLS# 582071</p>
    </div>
    <div class="divider"></div>
    <div class="company">
      <p class="corp">Pelvora Corporation, DBA<br>: Pelvora Home<br>Lending ™</p>
      <p class="corp-nmls">Company NMLS: 4817203</p>
      <p class="address">18 Caldwell Park Dr. Suite<br>210, Ashford, PA 19062</p>
    </div>
    <div class="reach">
      <p class="lines">CALL /TEXT/EMAIL DORIAN KELT<br>DKELT@PELVORAFUNDING.COM</p>
      <p class="phone">
        <svg class="phone-icon" viewBox="0 0 24 24" aria-hidden="true"><circle cx="12" cy="12" r="10.5" fill="none" stroke="var(--swoosh-blue)" stroke-width="1.6"/><path d="M8.6 6.5c.4 0 .7.2.8.6l.7 1.8c.1.3 0 .7-.3.9l-.9.7c.6 1.3 1.6 2.3 2.9 2.9l.7-.9c.2-.3.6-.4.9-.3l1.8.7c.4.1.6.4.6.8v1.4c0 .6-.5 1-1.100 1C10.2 16.6 7.4 13.8 7 9.7c0-.6.4-1.1 1-1.1z" fill="var(--swoosh-blue)"/></svg>
        502-647-2913
      </p>
    </div>
  </section>

  <section class="card back">
    <svg class="card-bg" viewBox="0 0 634 491">
      <defs>
        <linearGradient id="loan-tones" x1="0" y1="0" x2="0" y2="1">
          <stop offset="0" stop-color="#f6f1ea"/>
          <stop offset=".3" stop-color="#e6d8c2"/>
          <stop offset=".5" stop-color="#c9b690"/>
          <stop offset=".68" stop-color="#e3c3a2"/>
          <stop offset=".82" stop-color="#7f9460"/>
          <stop offset="1" stop-color="#43603b"/>
        </linearGradient>
      </defs>
      <path class="navy-panel" d="M0,190 L233,191 C270,250 340,320 366,433 L360,491 L0,491 Z" fill="var(--navy)"/>
      <path class="blue-swoosh" d="M245,212 C300,280 395,340 393,420 L389,491 L362,491 C370,420 330,300 245,212 Z" fill="var(--swoosh-blue)"/>
      <path class="loan-photo" role="img" aria-label="Photo of hands exchanging a small wooden house and a money bag" d="M0,0 L350,0 C365,70 330,130 276,163 C230,185 190,194 140,194 C80,194 35,185 0,169 Z" fill="url(#loan-tones)"/>
      <path class="sky-band" d="M0,169 C35,185 80,194 140,194 C190,194 230,185 276,163 L262,178 C220,198 180,210 140,210 C80,210 30,198 0,182 Z" fill="var(--sky)"/>
      <path class="orange-swoosh" d="M350,0 L366,0 C380,80 340,140 270,172 L276,163 C330,130 365,70 350,0 Z" fill="var(--orange)"/>
      <path class="orange-line" d="M209,194 C260,260 350,330 363,420" fill="none" stroke="var(--orange)" stroke-width="2"/>
      <path class="cta-band" d="M0,430 L369,430 L362,491 L0,491 Z" fill="var(--orange)"/>
    </svg>

    <h2 class="headline">HOME LOANS available for business<br>owners without traditional tax returns.</h2>
    <div class="stamp"></div>
    <div class="address-line" style="top:259px"></div>
    <div class="address-line" style="top:288px"></div>
    <div class="address-line" style="top:317px"></div>

    <ol class="disclosures">
      <li><span class="num">1.</span><span>Amount of the represented<br>loan.</span></li>
      <li><span class="num">2.</span><span>Repayment term in years of the<br>represented loan.</span></li>
      <li><span class="num">3.</span><span>Prepayment terms.</span></li>
      <li><span class="num">4.</span><span>If the advertised rate may increase,<br>the ad must state: "Advertised rate<br>may increase"</span></li>
      <li><span class="num">5.</span><span>Statement : "Restrictions may apply.<span class="note">Programs not available in all areas."</span></span></li>
    </ol>

    <p class="cta">Call the loan officer
      <svg class="phone-icon" viewBox="0 0 24 24" aria-hidden="true"><circle cx="12" cy="12" r="10.5" fill="none" stroke="var(--navy)" stroke-width="1.8"/><path d="M8.6 6.5c.4 0 .7.2.8.6l.7 1.8c.1.3 0 .7-.3.9l-.9.7c.6 1.3 1.6 2.3 2.9 2.9l.7-.9c.2-.3.6-.4.9-.3l1.8.7c.4.1.6.4.6.8v1.4c0 .6-.5 1-1.1 1C10.2 16.6 7.4 13.8 7 9.7c0-.6.4-1.1 1-1.1z" fill="var(--navy)"/></svg>
      502.647.2913</p>
  </section>

</main>
</body>
</html>
```